Preferred pricing vendor

We are a plumbing company that has many services
-Boilers & Controls
-Plumbing & Heating
-HVAC & Refrigeration
-Preventative Maintenacne
-Gas fitting & Drain Cleaning

We primarily look after condo buildings, and our preferred service rates ($98, $93, or $88 depending on the contract) extend to all of our clients. So in essence, we look after the mechanical room and common equipment but our clients can call us in for drain cleaning or replacing a fixture in their suite. The discounted rates apply to the personal residence. We want a flyer to let them know they get a discount on our services. A one-pager we can send out to all of our contract clients.

Included source files for our letterhead and logo just so you can see the colours we go with.

Target Market(s)

Residential repairs, individual people, replacement of fixtures in-suite specific repairs

Requirements
Must have
• be colourful and attractive

```html
<!DOCTYPE html>
<html lang="en">
<head>
<meta charset="utf-8">
<title>Keystone Mechanical Inc – Preferred Rates Flyer</title>
<link rel="stylesheet" href="https://fonts.googleapis.com/css2?family=Nunito:wght@700;800&family=Saira+Condensed:ital,wght@1,800&display=swap">
<style>
  :root {
    --brand-blue: #1a6fc9;
    --bar-blue: #1f73c0;
    --brand-orange: #f05a28;
    --burst-red: #ff0f0a;
    --ink: #111418;
    --paper: #ffffff;
    --tick-green: #1ec46a;
    --headline-shadow: #555b63;
  }
  * { box-sizing: border-box; margin: 0; padding: 0; }
  html, body { width: 848px; height: 1200px; overflow: hidden; background: var(--paper); }
  .flyer { position: relative; width: 848px; height: 1200px; background: var(--paper); overflow: hidden; }

  .bar { position: absolute; height: 30px; }
  .bar--blue { left: 0; width: 561px; background: var(--bar-blue); }
  .bar--orange { left: 568px; width: 280px; background: var(--brand-orange); }
  .bar--top { top: 0; }
  .bar--bottom { top: 1170px; }

  .brand { position: absolute; top: 62px; left: 0; width: 848px; display: flex; flex-direction: column; align-items: center; }
  .brand__dot { width: 70px; height: 70px; border-radius: 50%; background: var(--brand-orange); margin-bottom: 22px; }
  .brand__name { font-family: "Nunito", sans-serif; font-weight: 800; font-size: 30px; color: var(--brand-blue); letter-spacing: 1px; }

  .headline-banner { position: absolute; top: 221px; left: 0; width: 848px; height: 137px; }
  .headline-banner svg { position: absolute; inset: 0; }
  .headline { position: absolute; inset: 0; display: flex; flex-direction: column; justify-content: center; align-items: center;
    font-family: "Saira Condensed", sans-serif; font-style: italic; font-weight: 800; font-size: 46px; line-height: 48px;
    color: var(--paper); text-shadow: 2px 2px 0 var(--headline-shadow); letter-spacing: -0.5px; }

  .services-panel { position: absolute; top: 358px; left: 0; width: 457px; height: 675px; background: var(--brand-orange); }
  .service-list { position: absolute; top: 392px; left: 37px; list-style: none; }
  .service-list li { display: flex; align-items: center; height: 30px; font-family: "Nunito", sans-serif; font-weight: 700;
    font-size: 21px; color: var(--paper); text-shadow: 1px 1px 1px rgba(0,0,0,.45); }
  .service-list svg { width: 22px; height: 22px; margin-right: 18px; flex: none; }

  .discount-burst { position: absolute; left: 17px; top: 538px; width: 392px; height: 392px; }
  .discount-text { position: absolute; left: 17px; top: 538px; width: 392px; height: 392px; display: flex; flex-direction: column;
    justify-content: center; align-items: center; font-family: "Saira Condensed", sans-serif; font-style: italic; font-weight: 800;
    font-size: 64px; line-height: 58px; color: var(--paper); text-shadow: 3px 3px 0 var(--headline-shadow); }

  .photo { position: absolute; left: 469px; width: 372px; }
  .photo--plumbing { top: 368px; height: 246px; background: linear-gradient(135deg, #e9ecef, #aab0b6 55%, #3a5e86); }
  .photo--rooftop { top: 624px; height: 247px; background: linear-gradient(160deg, #c9dcef, #9a8c84 50%, #6d6a68); }
  .photo--gauges { top: 884px; height: 150px; background: linear-gradient(120deg, #8f8a84, #c9b56a 45%, #2a5bb4); }

  .van { position: absolute; left: 26px; top: 885px; width: 493px; height: 187px; border-radius: 60px 90px 20px 20px;
    background: linear-gradient(180deg, #fbfbfb, #dcdcdc 75%, #8a8a8a); box-shadow: 0 10px 14px -6px rgba(0,0,0,.5); }

  .rates-band { position: absolute; top: 1044px; left: 0; width: 848px; height: 118px; background: var(--brand-blue); }
  .rates { position: absolute; top: 1098px; left: 27px; width: 800px; font-family: "Saira Condensed", sans-serif; font-style: italic;
    font-weight: 800; font-size: 30px; line-height: 36px; color: var(--ink); white-space: nowrap; }
</style>
</head>
<body>
<main class="flyer">
  <div class="bar bar--top bar--blue"></div>
  <div class="bar bar--top bar--orange"></div>

  <header class="brand">
    <div class="brand__dot"></div>
    <div class="brand__name">KEYSTONE MECHANICAL INC</div>
  </header>

  <section class="headline-banner">
    <svg width="848" height="137" viewBox="0 0 848 137"><polygon points="69,0 779,0 817,137 16,137" fill="#1a6fc9"/></svg>
    <h1 class="headline"><span>WE ARE A PLUMBING COMPANY</span><span>THAT HAS MANY SERVICES</span></h1>
  </section>

  <div class="services-panel"></div>
  <ul class="service-list">
    <li><svg viewBox="0 0 22 22"><rect x="1.5" y="1.5" width="19" height="19" rx="3" fill="none" stroke="#1ec46a" stroke-width="3"/><path d="M5 11l5 5 9-11" fill="none" stroke="#1ec46a" stroke-width="3.5" stroke-linecap="round"/></svg>Boilers &amp; Controls</li>
    <li><svg viewBox="0 0 22 22"><rect x="1.5" y="1.5" width="19" height="19" rx="3" fill="none" stroke="#1ec46a" stroke-width="3"/><path d="M5 11l5 5 9-11" fill="none" stroke="#1ec46a" stroke-width="3.5" stroke-linecap="round"/></svg>Plumbing &amp; Heating</li>
    <li><svg viewBox="0 0 22 22"><rect x="1.5" y="1.5" width="19" height="19" rx="3" fill="none" stroke="#1ec46a" stroke-width="3"/><path d="M5 11l5 5 9-11" fill="none" stroke="#1ec46a" stroke-width="3.5" stroke-linecap="round"/></svg>HVAC &amp; Refrigeration</li>
    <li><svg viewBox="0 0 22 22"><rect x="1.5" y="1.5" width="19" height="19" rx="3" fill="none" stroke="#1ec46a" stroke-width="3"/><path d="M5 11l5 5 9-11" fill="none" stroke="#1ec46a" stroke-width="3.5" stroke-linecap="round"/></svg>Preventative Maintenacne</li>
    <li><svg viewBox="0 0 22 22"><rect x="1.5" y="1.5" width="19" height="19" rx="3" fill="none" stroke="#1ec46a" stroke-width="3"/><path d="M5 11l5 5 9-11" fill="none" stroke="#1ec46a" stroke-width="3.5" stroke-linecap="round"/></svg>Gas fitting &amp; Drain Cleaning</li>
  </ul>

  <svg class="discount-burst" viewBox="-100 -100 200 200">
    <polygon fill="#ff0f0a" points="100,0 82.4,16.4 92.4,38.3 69.8,46.7 70.7,70.7 46.7,69.8 38.3,92.4 16.4,82.4 0,100 -16.4,82.4 -38.3,92.4 -46.7,69.8 -70.7,70.7 -69.8,46.7 -92.4,38.3 -82.4,16.4 -100,0 -82.4,-16.4 -92.4,-38.3 -69.8,-46.7 -70.7,-70.7 -46.7,-69.8 -38.3,-92.4 -16.4,-82.4 0,-100 16.4,-82.4 38.3,-92.4 46.7,-69.8 70.7,-70.7 69.8,-46.7 92.4,-38.3 82.4,-16.4"/>
  </svg>
  <p class="discount-text"><span>SPECIAL</span><span>DISCOUNT</span><span>AVAILABLE</span></p>

  <div class="photo photo--plumbing" role="img" aria-label="Photo of a plumber tightening a chrome sink trap with a wrench"></div>
  <div class="photo photo--rooftop" role="img" aria-label="Photo of two technicians in hard hats servicing a rooftop air conditioning unit"></div>
  <div class="photo photo--gauges" role="img" aria-label="Photo of a technician in a hard hat checking pipes and gauges in a mechanical room"></div>

  <div class="rates-band"></div>
  <div class="van" role="img" aria-label="Photo of a white company service van"></div>
  <p class="rates">SERVICE RATES: ($98, $93, OR $88 DEPENDING ON THE CONTRACT)</p>

  <div class="bar bar--bottom bar--blue"></div>
  <div class="bar bar--bottom bar--orange"></div>
</main>
</body>
</html>
```